Option Sheet

We need a one page option sheet with a left to right reading of the five options. It should be a one sheet, multiple colors and definitive separations between options This is used in a sales consultation. Backround or colors not in option need to have the follow RGB value (5 red, 20 green, 63 blue)

We added a smaller text file, please change that point

Target Market(s)

Divorce

Industry/Entity Type

Legal

Requirements
Must have
• 1) All five options left to right
• 2)language included in sheet

```html
<!DOCTYPE html>
<html lang="en">
<head>
<meta charset="utf-8">
<title>Five Options – Divorce</title>
<link href="https://fonts.googleapis.com/css2?family=Bebas+Neue&family=Roboto:wght@400;500&display=swap" rel="stylesheet">
<style>
  :root {
    --navy: rgb(5, 20, 63);
    --navy-deep: #0c1344;
    --navy-tint: #17225a;
    --orange: #e8891c;
    --white: #ffffff;
    --divider: #e4e5ea;
    --header-bg: #f7f7f8;
  }
  * { box-sizing: border-box; margin: 0; padding: 0; }
  html, body { width: 1179px; height: 1200px; overflow: hidden; }
  body { background: var(--navy); font-family: "Roboto", Arial, sans-serif; }

  .sheet { width: 1179px; height: 1200px; display: flex; flex-direction: column; }

  .sheet-header {
    height: 230px; background: var(--header-bg); position: relative;
  }
  .headline {
    position: absolute; left: 74px; top: 42px;
    font-family: "Bebas Neue", Impact, sans-serif; font-size: 168px; line-height: 1;
    color: var(--navy-deep); letter-spacing: 1px;
  }
  .headline .accent { color: var(--orange); margin-right: 18px; }
  .site-url {
    position: absolute; left: 860px; top: 120px;
    font-size: 17px; font-weight: 500; color: var(--navy-deep); letter-spacing: .3px;
  }
  .topic-band {
    position: absolute; left: 838px; right: 0; top: 142px; height: 36px;
    background: var(--orange); padding-left: 22px;
    font-family: "Roboto", Arial, sans-serif; font-weight: 500; font-size: 25px;
    line-height: 36px; letter-spacing: 7px; color: var(--navy-deep);
  }

  .options { flex: 1; display: flex; gap: 4px; background: var(--divider); }
  .option {
    flex: 1; background: var(--navy); position: relative; overflow: hidden;
  }
  .option-tab {
    height: 56px; background: var(--orange); position: relative;
    font-family: "Bebas Neue", Impact, sans-serif; font-size: 40px; line-height: 58px;
    text-align: center; color: var(--navy-deep); letter-spacing: 1px;
  }
  .option-tab::after {
    content: ""; position: absolute; left: 50%; bottom: -16px; margin-left: -18px;
    border-left: 18px solid transparent; border-right: 18px solid transparent;
    border-top: 16px solid var(--orange);
  }
  .option-name {
    height: 180px; display: flex; align-items: center; justify-content: center;
    padding-top: 30px; text-align: center;
    font-family: "Bebas Neue", Impact, sans-serif; font-size: 31px; line-height: 1.05;
    letter-spacing: 1.5px; color: var(--white);
  }
  .option-name.featured { font-size: 58px; line-height: .95; color: var(--orange); }

  .ribbon {
    display: block; width: 86%; height: 26px; background: var(--divider);
    clip-path: polygon(0 0, 100% 0, 94% 50%, 100% 100%, 0 100%);
    font-family: "Bebas Neue", Impact, sans-serif; font-size: 24px; line-height: 28px;
    letter-spacing: 1px; color: var(--navy-deep); text-align: center; padding-right: 12px;
  }
  .ribbon.featured { background: var(--orange); }

  .points { list-style: none; padding: 18px 14px 0 22px; }
  .points.advantages { height: 150px; }
  .option:last-child .points.advantages { height: auto; padding-bottom: 28px; }
  .points li {
    position: relative; padding-left: 28px; margin-bottom: 14px;
    font-size: 15px; line-height: 1.1; color: var(--white);
  }
  .points li::before {
    content: ""; position: absolute; left: 4px; top: 1px; width: 6px; height: 11px;
    border-right: 2px solid var(--orange); border-bottom: 2px solid var(--orange);
    transform: rotate(40deg);
  }

  .tile { position: absolute; background: var(--navy-tint); }
</style>
</head>
<body>
<main class="sheet">
  <header class="sheet-header">
    <h1 class="headline"><span class="accent">FIVE</span>OPTIONS</h1>
    <p class="site-url">WWW.WEBSITE.COM</p>
    <p class="topic-band">DIVORCE</p>
  </header>

  <section class="options">
    <article class="option">
      <h2 class="option-tab">OPTION 1</h2>
      <h3 class="option-name">DO<br>NOTHING</h3>
      <span class="ribbon">ADVANTAGES</span>
      <ul class="points advantages"><li>Stay married</li><li>No life Changes</li></ul>
      <span class="ribbon">DISADVANTAGES</span>
      <ul class="points"><li>Remain unhappy, depressed, anxious</li><li>Money and assets may disappear</li><li>What is going to change?</li></ul>
      <div class="tile" style="left:0;bottom:150px;width:40px;height:40px"></div>
      <div class="tile" style="left:50px;bottom:150px;width:40px;height:40px"></div>
      <div class="tile" style="left:0;bottom:90px;width:40px;height:40px"></div>
      <div class="tile" style="left:70px;bottom:0;width:150px;height:120px"></div>
    </article>

    <article class="option">
      <h2 class="option-tab">OPTION 2</h2>
      <h3 class="option-name">GO TO<br>COUNSELING</h3>
      <span class="ribbon">ADVANTAGES</span>
      <ul class="points advantages"><li>Reconcile marriage</li><li>Help make a better life</li></ul>
      <span class="ribbon">DISADVANTAGES</span>
      <ul class="points"><li>Past issues are highlighted and may drudge up old wounds</li><li>It may just clarify the reasons you need to separate and/or divorce</li><li>Both parties must be invested and willing to participate</li></ul>
      <div class="tile" style="left:60px;bottom:100px;width:30px;height:30px"></div>
      <div class="tile" style="left:100px;bottom:100px;width:30px;height:30px"></div>
      <div class="tile" style="left:60px;bottom:60px;width:30px;height:30px"></div>
      <div class="tile" style="left:110px;bottom:0;width:120px;height:90px"></div>
    </article>

    <article class="option">
      <h2 class="option-tab">OPTION 3</h2>
      <h3 class="option-name">DO IT<br>YOURSELF</h3>
      <span class="ribbon">ADVANTAGES</span>
      <ul class="points advantages"><li>No attorney fees</li></ul>
      <span class="ribbon">DISADVANTAGES</span>
      <ul class="points"><li>People often find that what is “fair,” may in fact, not be truly fair</li><li>Often times, people do not know the risks</li><li>Complicated legal system</li><li>Unsure how to complete the necessary paper-work and meet the deadlines</li></ul>
      <div class="tile" style="left:100px;bottom:60px;width:20px;height:20px"></div>
      <div class="tile" style="left:126px;bottom:60px;width:20px;height:20px"></div>
      <div class="tile" style="left:100px;bottom:32px;width:20px;height:20px"></div>
      <div class="tile" style="left:140px;bottom:0;width:90px;height:50px"></div>
    </article>

    <article class="option">
      <h2 class="option-tab">OPTION 4</h2>
      <h3 class="option-name">LIMITED<br>REPRESENTATION</h3>
      <span class="ribbon">ADVANTAGES</span>
      <ul class="points advantages"><li>Balance between going alone and our limited involvement in the case</li></ul>
      <span class="ribbon">DISADVANTAGES</span>
      <ul class="points"><li>Our terms may not benefit from our legal knowledge</li><li>The legal conse-quences of your legal documents will not be explained to you so that you can formulate a plan for handling the rest of your case.</li><li>Your spouse or other parties may cause your legal fees to increase significantly without action on your part</li></ul>
      <div class="tile" style="left:140px;bottom:40px;width:16px;height:16px"></div>
      <div class="tile" style="left:160px;bottom:40px;width:16px;height:16px"></div>
      <div class="tile" style="left:140px;bottom:20px;width:16px;height:16px"></div>
      <div class="tile" style="left:170px;bottom:0;width:60px;height:36px"></div>
    </article>

    <article class="option">
      <h2 class="option-tab">OPTION 5</h2>
      <h3 class="option-name featured">HIRE<br>US</h3>
      <span class="ribbon featured">ADVANTAGES</span>
      <ul class="points advantages"><li>Gain the full benefits of our experience</li><li>Have a team of Harbor Family Law attorneys</li><li>Often saves you money in the long run</li><li>Save you time and energy</li></ul>
      <span class="ribbon featured">DISADVANTAGES</span>
      <ul class="points"><li>Initial Cost</li></ul>
      <div class="tile" style="left:100px;bottom:150px;width:40px;height:40px"></div>
      <div class="tile" style="left:150px;bottom:150px;width:40px;height:40px"></div>
      <div class="tile" style="left:200px;bottom:90px;width:30px;height:40px"></div>
      <div class="tile" style="left:0;bottom:0;width:130px;height:120px"></div>
    </article>
  </section>
</main>
</body>
</html>
```